Resume for higher management position in a mechanical/consultant industries application*

I would like to use this resume for getting a higher position interview possibilities. My skills are multi-cultural negotiation, mechanical industry sales, outsourcing to Asia, ability to manage the agent/reseller system, well team player. multi-language Chinese/English/German specialized. Please make the design, professional, comfortable to read atmosphere.

Target Market(s)

management position, sales related

Font styles to use
Serif
Sans Serif

```html
<!DOCTYPE html>
<html lang="en">
<head>
<meta charset="utf-8">
<title>Wei-Lun Hsu — Resume</title>
<link href="https://fonts.googleapis.com/css2?family=Montserrat:wght@300;400;500;600;700&display=swap" rel="stylesheet">
<style>
  :root{
    --backdrop:#95a3b1;
    --paper:#ffffff;
    --band:#ecedf0;
    --navy:#0b2c55;
    --accent:#1f5f8f;
    --ink:#3a3f47;
    --muted:#8a8f96;
    --rule:#2f6a96;
    --body-text:#555a62;
  }
  *{box-sizing:border-box;margin:0;padding:0}
  html,body{width:1200px;height:1200px;overflow:hidden}
  body{background:var(--backdrop);font-family:"Montserrat",sans-serif;color:var(--ink);position:relative}
  .resume{position:absolute;left:204px;top:40px;width:792px;height:1120px;background:var(--paper);display:flex;box-shadow:0 8px 30px rgba(20,30,45,.25)}
  .sidebar{width:285px;height:100%;background:linear-gradient(180deg,#8a8c90 0%,#7f8590 30%,#6f7f92 45%,#2b5679 65%,var(--navy) 100%);color:#fff;display:flex;flex-direction:column;padding:0 0 36px}
  .portrait{height:370px;width:100%;background:radial-gradient(ellipse at 50% 55%,#a7adb7 0%,#8d9199 55%,#858890 100%)}
  .about{padding:28px 26px 0 34px}
  .side-heading{display:flex;align-items:center;gap:10px;font-size:13px;letter-spacing:.28em;font-weight:500;margin-bottom:12px}
  .side-heading::after{content:"";flex:1;height:1px;background:rgba(255,255,255,.7)}
  .about p{font-size:10.3px;line-height:1.5;font-weight:300}
  .contact{margin-top:auto;padding:0 26px 0 34px}
  .contact dt{font-size:10.5px;font-weight:600;margin-top:8px}
  .contact dd{font-size:10px;font-weight:300;opacity:.9}
  .main{flex:1;display:flex;flex-direction:column}
  .masthead{background:var(--band);height:200px;padding:70px 40px 0 44px}
  .name{font-size:48px;line-height:1;color:#8b8f95;font-weight:600;letter-spacing:-.01em}
  .name .family{font-weight:300}
  .role{color:var(--accent);font-size:19px;font-weight:300;margin-top:10px}
  .body{padding:28px 40px 0 44px;display:flex;flex-direction:column;gap:26px}
  .section-heading{display:flex;align-items:center;gap:12px;font-size:14px;letter-spacing:.26em;color:var(--muted);font-weight:500;margin-bottom:10px}
  .section-heading::after{content:"";flex:1;height:1px;background:var(--rule)}
  .skills li{list-style:none;font-size:11.5px;line-height:1.45;font-weight:600;color:var(--ink);margin-bottom:8px}
  .skills .label{color:var(--accent)}
  .job{margin-bottom:14px;font-size:11.2px;line-height:1.5}
  .job-head{font-weight:600;color:var(--ink)}
  .date{color:var(--accent);font-weight:700}
  .job p{font-weight:300;color:var(--body-text)}
  .edu li{list-style:none;font-size:11.2px;line-height:1.5;font-weight:600;margin-bottom:4px}
  .edu .field{font-weight:300;color:var(--body-text)}
</style>
</head>
<body>
<article class="resume">
  <aside class="sidebar">
    <div class="portrait" role="img" aria-label="Portrait photo of the candidate in a light blue shirt holding a folder"></div>
    <section class="about">
      <h2 class="side-heading">ABOUT</h2>
      <p>Mandarin Chinese/ German/ English speaker, real machining experiences, OEM skills, trade skill, global sourcing. Currently I am a "Sales manager Asia" of a top German rotary table company. I am in charge of four countries Japan, China, South Korea and Taiwan with 3 agents, more than 20 salesmen team. As a director of manufacturing, I have more than 5 years professional experiences in manufacturing metal components by different CNC-machines. I am capable of coding CNC GM-code, designing the working path of different parts and managing the whole process. I have well-understanding of mechanical outsourcing ecosystem in Taiwan. With deep knowledge of outsourcing metal components to different suppliers in Taiwan. Familiar with coordinating with different industrial processes in order to build the final products (Black oxidizing, Different anodizing, Chemical polishing, Manganese phosphate coating, Heat treatment, and different grinding methods). Especially love to build prototype in order to get a high profitable potential products (from zero to one).</p>
    </section>
    <section class="contact">
      <h2 class="side-heading">CONTACT</h2>
      <dl>
        <dt>Address</dt><dd>xxxxxxxx, Germany</dd>
        <dt>Phone number</dt><dd>+xxxxxxxxxxx</dd>
        <dt>Email</dt><dd>xxxxxxxxx@mailbox.com</dd>
      </dl>
    </section>
  </aside>
  <main class="main">
    <header class="masthead">
      <h1 class="name">Wei-Lun <span class="family">Hsu</span></h1>
      <p class="role">Sales manager Asia</p>
    </header>
    <div class="body">
      <section class="skills">
        <h2 class="section-heading">SKILLS</h2>
        <ul>
          <li>MBA degree from VBS, Accademia Politecnica di Verona.</li>
          <li><span class="label">Specialties:</span> Great experiences in handling business with Chinese - cultural business firms.</li>
          <li>Multi-national corporation skills( especially in Chinese-speaking market)</li>
          <li><span class="label">Multi-language skill:</span> native Chinese speaker/ advanced English/ advanced German</li>
        </ul>
      </section>
      <section class="experience">
        <h2 class="section-heading">EXPERIENCE</h2>
        <div class="job">
          <div class="job-head"><span class="date">2018-now</span> | Sales Manager Asiaxxxxxxxxx</div>
          <p>Currently, leading 3 major dealers in Taiwan, Mainland China, South Korea and Japan with more than 20 salesmen team. Rotavia provides rotary tables, trunnions and 2 axis rotary tilt units shall have the best possible technical characteristics in the smallest possible space, is the principle model for our dividing heads -engineering -manufacturing -and assembly.</p>
        </div>
        <div class="job">
          <div class="job-head"><span class="date">2012-2017</span> | Weissberg Precision Machinery Company | Director of Manufacturing</div>
          <p>Using CNC turn/mill machine to manufacture any mechanical components as customers want. Also providing great total solutions for our clients. Photos shown in my online profile are my products which are made by CNC turn-milling dual spindles machines(trophy is programmed by CAM).</p>
        </div>
        <div class="job">
          <div class="job-head"><span class="date">2012 Apr- 2012 Nov</span> | Blue Harbor Import Mannheim Germany | Marketing Analyst</div>
          <p>Help Blue Harbor Import to build their sales/marketing strategy for the new launched product "Slidrex" in central Europe.</p>
        </div>
        <div class="job">
          <div class="job-head"><span class="date">2011 Oct-2012 Mar</span> | Calvera Group Bergamo Italy | External consultant</div>
          <p>To improve the Orbit solution(ERP system) of Calvera with re-organized procurement process and new standardized KPIs.</p>
        </div>
      </section>
      <section class="edu">
        <h2 class="section-heading">EDUCATION</h2>
        <ul>
          <li><span class="date">2011-2012</span> | MBA, Accademia Politecnica di Verona, Italy</li>
          <li><span class="date">2005-2009</span> | Lan-Shan Technical University | Bachelor of Chemical <span class="field">engineering</span></li>
        </ul>
      </section>
    </div>
  </main>
</article>
</body>
</html>
```